Stickers to put on my honeyglasses

Stickers for my honey glasses.
Only a single sticker on the front. Same should have a stripe on the top side which goes above the lid to show if the glass was opened.
Size of the main part should be 55mm high and max. 100 mm wide.
The stripe on the top should be 70mm long.
I added a Picture of another producer which uses the same glass as I do.
I should say: 'e Lendorf Glas Hunneg'. which means 'another glass of honey. 'Hunneg' should be mainly visible and therefore very large. 'e Lendorf Glas' should be less visible and therefore smaller above the 'Hunneg'
- It needs to contain the quantity : '500gr'
- It needs to contain my Name and address: 'Marc Lendorf, 38, rue Ferd Lusang, L-9241 Miersch' (This should be small and not to visible)
- It needs to conatin a validity Line: ´Am beschte virum:` (With enough space so I can add a date by hand)
- It needs to say: 'dréchen, kill andäischterstockéieren' (to store it dry cold and dark)

```html
<!DOCTYPE html>
<html lang="lb">
<head>
<meta charset="utf-8">
<title>e Lendorf Glas Hunneg – Etikett</title>
<link rel="stylesheet" href="https://fonts.googleapis.com/css2?family=Playfair+Display:ital,wght@0,900;1,700;1,900&family=Quicksand:wght@500&family=Libre+Franklin:wght@400;700;900&display=swap">
<style>
  :root {
    --page: #ffffff;
    --label-cream: #fbf8f1;
    --label-edge: #f0b92a;
    --comb-tint: #f7ecd0;
    --gold-light: #f7cf5e;
    --gold: #f0ad1a;
    --gold-deep: #e29a10;
    --olive: #6e6a1c;
    --ink: #111111;
    --bee-tone: #3a2c12;
    --bloom-tone: #e7c9d4;
    --leaf-tone: #cfdca8;
  }
  * { margin: 0; padding: 0; box-sizing: border-box; }
  html, body { width: 1200px; height: 1000px; overflow: hidden; background: var(--page); }
  .canvas { position: relative; width: 1200px; height: 1000px; }
  .label-outline { position: absolute; left: 0; top: 0; }

  .bee-art {
    position: absolute; left: 552px; top: 530px; width: 96px; height: 104px;
    border-radius: 50% 50% 45% 45%;
    background: radial-gradient(circle at 60% 55%, var(--bee-tone) 0 28%, #d9a52a 40%, rgba(240,230,200,.6) 62%, transparent 72%);
  }
  .meadow-art {
    position: absolute; left: 432px; top: 815px; width: 330px; height: 104px;
    clip-path: polygon(0 0, 100% 0, 89% 100%, 11% 100%);
    background: linear-gradient(180deg, rgba(231,201,212,0) 0%, var(--bloom-tone) 40%, var(--leaf-tone) 100%);
  }

  .tagline {
    position: absolute; left: 380px; width: 440px; top: 664px; text-align: center;
    font-family: "Playfair Display", serif; font-style: italic; font-weight: 700;
    font-size: 31px; letter-spacing: 1px; color: var(--gold);
  }
  .product-name {
    position: absolute; left: 370px; width: 460px; top: 675px; text-align: center;
    font-family: "Playfair Display", serif; font-weight: 900; font-size: 122px; line-height: 1.1;
    background: linear-gradient(180deg, var(--gold-deep) 0%, var(--gold) 45%, var(--gold-light) 100%);
    -webkit-background-clip: text; background-clip: text; color: transparent;
    filter: drop-shadow(3px 4px 3px rgba(150, 100, 20, .35));
  }
  .quantity {
    position: absolute; left: 520px; width: 160px; top: 922px; text-align: center;
    font-family: "Playfair Display", serif; font-weight: 900; font-size: 25px; color: var(--gold);
  }

  .producer-info { position: absolute; left: 231px; top: 794px; font-family: "Quicksand", sans-serif; font-weight: 500; color: var(--olive); font-size: 16px; line-height: 17px; }
  .storage-note { margin-bottom: 18px; }
  .address { margin-left: 4px; line-height: 20px; }
  .best-before { position: absolute; left: 235px; top: 900px; font-family: "Quicksand", sans-serif; font-weight: 500; color: var(--olive); font-size: 16px; }

  .nutrition-facts {
    position: absolute; left: 830px; top: 785px; width: 139px; height: 173px;
    background: #fff; border: 1px solid var(--ink); padding: 2px 3px;
    font-family: "Libre Franklin", sans-serif; color: var(--ink); font-size: 5.4px; line-height: 1.25;
  }
  .nf-title { font-weight: 900; font-size: 15px; line-height: 15px; }
  .nf-row { display: flex; justify-content: space-between; border-top: .5px solid var(--ink); padding: .6px 0; }
  .nf-serving { font-weight: 700; font-size: 7.5px; border-top: none; }
  .nf-thick { border-bottom: 5px solid var(--ink); }
  .nf-cal { font-weight: 900; font-size: 11px; line-height: 12px; border-top: none; align-items: flex-end; }
  .nf-cal .nf-cal-value { font-size: 17px; line-height: 16px; }
  .nf-mid { border-bottom: 2.5px solid var(--ink); }
  .nf-dv { text-align: right; font-weight: 700; font-size: 4.4px; border-top: .5px solid var(--ink); }
  .nf-indent { padding-left: 6px; }
  .nf-bold { font-weight: 700; }
  .nf-foot { border-top: 4px solid var(--ink); padding-top: 2px; font-size: 3.8px; line-height: 1.3; }
</style>
</head>
<body>
<main class="canvas">
  <svg class="label-outline" width="1200" height="1000" viewBox="0 0 1200 1000" aria-hidden="true">
    <defs>
      <linearGradient id="combWash" x1="0" y1="0" x2="0" y2="1">
        <stop offset="0" stop-color="var(--comb-tint)"/>
        <stop offset="1" stop-color="var(--label-cream)"/>
      </linearGradient>
    </defs>
    <path d="M559 30 H635 L667 62 V548 H946 Q972 548 972 574 V937 Q972 963 946 963 H247 Q221 963 221 937 V574 Q221 548 247 548 H527 V62 Z"
          fill="url(#combWash)" stroke="var(--label-edge)" stroke-width="1.5"/>
    <polygon points="468,591 701,591 786,756 701,921 468,921 384,756"
             fill="var(--label-cream)" stroke="var(--label-edge)" stroke-width="2"/>
  </svg>

  <div class="bee-art" role="img" aria-label="Illustration of a honey bee"></div>
  <div class="meadow-art" role="img" aria-label="Illustration of meadow flowers: clover, lavender and daisies"></div>

  <p class="tagline">e Lendorf Glas</p>
  <h1 class="product-name">Hunneg</h1>
  <p class="quantity">500gr</p>

  <div class="producer-info">
    <p class="storage-note">dréchen, kill<br>andäischterstockéieren</p>
    <p class="address">Marc Lendorf, 38,<br>rue Ferd Lusang,<br>L-9241 Miersch</p>
  </div>
  <p class="best-before">Am beschte virum:</p>

  <section class="nutrition-facts" aria-label="Nutrition Facts">
    <div class="nf-title">Nutrition Facts</div>
    <div>16 servings per container</div>
    <div class="nf-row nf-serving nf-thick"><span>Serving Size</span><span>1 tbsp (21g)</span></div>
    <div class="nf-bold" style="font-size:4.4px">Amount Per Serving</div>
    <div class="nf-row nf-cal nf-mid"><span>Calories</span><span class="nf-cal-value">60</span></div>
    <div class="nf-dv">% Daily Value*</div>
    <div class="nf-row"><span><b>Total Fat</b> 0g</span><b>0%</b></div>
    <div class="nf-row"><span><b>Cholesterol</b> 0mg</span><b>0%</b></div>
    <div class="nf-row"><span><b>Sodium</b> 0mg</span><b>0%</b></div>
    <div class="nf-row"><span><b>Total Carbohydrate</b> 17g</span><b>6%</b></div>
    <div class="nf-row nf-indent"><span>Dietary Fiber 0g</span><b>0%</b></div>
    <div class="nf-row nf-indent"><span>Total Sugars 17g</span><span></span></div>
    <div class="nf-row"><span></span><b>34%</b></div>
    <div class="nf-row"><span><b>Protein</b> 0g</span><span></span></div>
    <div class="nf-foot">*The % Daily Value (DV) tells you how much a nutrient in a serving of food contributes to a daily diet. 2,000 calories a day is used for general nutrition advice.</div>
  </section>
</main>
</body>
</html>
```